Postcard Design

business name: COZY HOUR KEEPER. I am a mother of 2 well adjusted, successful teenage boys. I decided to start this company caring for kids who are home sick, unable to go to daycare or school, and when their parent cant stay home with them. I was also a career woman for many years, with no friends available or family nearby to help when i was in an emergency situation for childcare. I know how stressful it can be when a child gets sick suddenly and unexpectedly. I would like to help out those parents in need, that have pressing schedules and a sick child at home that they really want to take care of, but cant due to their work pressures and priorities. I want parents to know that their child is safe and I can help them when in need, at last minute. The design should show the child is safe and well cared for and the parent is at ease, able to accomplish their obligations. I have also founded a nonprofit environmental education program in which I teach children in youth summer camps. I have taught creativity arts combined with science curriculum in kindergarten to 8th grade non-formal teaching for the past 5 years. This is a small community, and many people know me. I will be handing out these postcards to local daycares and people I know.

Industry/Entity Type

Business

```html
<!DOCTYPE html>
<html lang="en">
<head>
<meta charset="utf-8">
<title>Cozy Hour Keeper – Postcard</title>
<link rel="stylesheet" href="https://fonts.googleapis.com/css2?family=Arimo:ital,wght@0,400;0,700;1,400&family=Lora:ital,wght@1,500&display=swap">
<style>
  :root {
    --page: #ecebe8;
    --orange: #de5a27;
    --teal: #1a9fae;
    --grey-text: #5f5f5f;
    --cream: #ede2b0;
    --tile-green: #c9d8b5;
    --tile-blue: #b6ccc8;
    --tile-orange: #f3b57a;
    --tile-pink: #f1cfbf;
    --tile-peach: #f6d7a9;
    --panel-white: #ffffff;
    --panel-mist: #f4f5f3;
    --rule: #b9b9b9;
  }
  * { box-sizing: border-box; margin: 0; padding: 0; }
  html, body { width: 936px; height: 1200px; overflow: hidden; }
  body {
    background: var(--page);
    font-family: "Arimo", Arial, sans-serif;
    position: relative;
  }
  .card {
    position: absolute;
    width: 664px;
    height: 516px;
    overflow: hidden;
    background: var(--cream);
    box-shadow: 0 4px 14px rgba(0,0,0,.18);
  }
  .card--front { left: 71px; top: 62px; }
  .card--back { left: 169px; top: 632px; background: var(--panel-white); }

  .tiles { position: absolute; left: 0; top: 0; }
  .title-box {
    position: absolute;
    background: var(--orange);
    border: 4px solid #fff;
    color: #fff;
    text-align: center;
    box-shadow: 0 2px 6px rgba(0,0,0,.2);
  }
  .title-box__main {
    display: block;
    font-weight: 700;
    font-size: 38px;
    letter-spacing: .5px;
    line-height: 1;
  }
  .title-box__script {
    display: block;
    font-family: "Lora", Georgia, serif;
    font-style: italic;
    font-weight: 500;
    font-size: 44px;
    line-height: 1;
    margin-top: 4px;
  }

  /* front */
  .front-panel {
    position: absolute;
    left: 14px; top: 224px;
    width: 349px; height: 292px;
    background: var(--panel-white);
  }
  .front-title { left: 38px; top: 60px; width: 246px; height: 164px; padding-top: 36px; transform: rotate(-1.5deg); }
  .photo-frame {
    position: absolute;
    left: 278px; top: 40px;
    width: 374px; height: 258px;
    background: #fff;
    padding: 8px;
    transform: rotate(3deg);
    box-shadow: 0 3px 8px rgba(0,0,0,.25);
  }
  .photo-frame__fill {
    width: 100%; height: 100%;
    background: linear-gradient(120deg, #e7d2b4 0%, #c9a278 30%, #dfe3ea 60%, #a9bcd8 100%);
  }
  .care-list {
    position: absolute;
    left: 28px; top: 26px;
    width: 310px;
  }
  .care-list__lead { color: var(--teal); font-size: 20px; margin-bottom: 8px; }
  .care-list ul { list-style: none; }
  .care-list li {
    position: relative;
    padding-left: 20px;
    color: var(--grey-text);
    font-size: 16.5px;
    line-height: 1.6;
  }
  .care-list li svg { position: absolute; left: 0; top: 7px; }
  .blocks-art {
    position: absolute;
    left: 4px; top: 172px;
    width: 104px; height: 88px;
    background: linear-gradient(135deg, #e8c24a 0%, #c7463d 35%, #4f8fc8 65%, #6aa94f 100%);
    border-radius: 4px;
  }
  .reassure {
    position: absolute;
    left: 112px; top: 180px;
    width: 226px;
    color: var(--grey-text);
    font-style: italic;
    font-size: 15.5px;
    line-height: 1.2;
    text-align: center;
  }
  .front-callout {
    position: absolute;
    left: 388px; top: 330px;
    width: 276px;
    text-align: center;
    color: var(--orange);
    font-size: 20px;
    line-height: 1.4;
  }
  .contact-box {
    position: absolute;
    background: var(--orange);
    color: #fff;
    text-align: center;
    font-weight: 700;
  }
  .contact-box--front {
    left: 381px; top: 414px; width: 290px; height: 110px;
    border: 5px solid #fff;
    padding: 10px 14px 0 0;
  }
  .contact-box__name { font-size: 22px; line-height: 1.3; }
  .contact-box__phone { font-size: 23px; line-height: 1.3; display: inline-flex; align-items: center; gap: 8px; }

  /* back */
  .back-left { position: absolute; left: 0; top: 0; width: 411px; height: 516px; background: var(--cream); }
  .back-title { left: 36px; top: 29px; width: 326px; height: 140px; padding-top: 24px; transform: rotate(-1deg); }
  .back-panel {
    position: absolute;
    left: 15px; top: 156px;
    width: 396px; height: 264px;
    background: var(--panel-mist);
    text-align: center;
    padding: 42px 20px 0 20px;
  }
  .back-panel__headline { color: var(--teal); font-weight: 700; font-size: 20px; }
  .back-panel__message {
    color: var(--grey-text);
    font-style: italic;
    font-size: 15px;
    line-height: 1.25;
    margin: 24px 14px 0;
  }
  .back-panel__experience { color: var(--orange); font-weight: 700; font-size: 17.5px; margin-top: 36px; }
  .contact-box--back { left: 0; top: 420px; width: 382px; height: 96px; padding-top: 18px; }
  .stamp-box { position: absolute; left: 550px; top: 24px; width: 97px; height: 59px; border: 1.5px solid var(--rule); }
  .address-line { position: absolute; left: 419px; width: 228px; height: 0; border-top: 1.5px solid var(--rule); }
</style>
</head>
<body>

<!-- Front of postcard -->
<section class="card card--front">
  <svg class="tiles" width="664" height="300" aria-hidden="true">
    <rect x="0" y="0" width="664" height="300" fill="var(--cream)"/>
    <rect x="0" y="0" width="150" height="140" fill="var(--tile-green)"/>
    <rect x="0" y="150" width="60" height="90" fill="var(--tile-peach)"/>
    <rect x="160" y="0" width="115" height="65" fill="var(--tile-blue)"/>
    <rect x="285" y="0" width="120" height="55" fill="var(--tile-orange)"/>
    <rect x="412" y="0" width="120" height="45" fill="var(--tile-green)"/>
    <rect x="540" y="0" width="40" height="70" fill="var(--tile-blue)"/>
    <rect x="590" y="0" width="74" height="70" fill="var(--tile-pink)"/>
    <rect x="590" y="80" width="74" height="200" fill="var(--tile-green)"/>
  </svg>

  <div class="photo-frame">
    <div class="photo-frame__fill" role="img" aria-label="Photo of a young child in bed playing doctor with a bandaged teddy bear"></div>
  </div>

  <div class="front-panel">
    <div class="care-list">
      <p class="care-list__lead">Caring for kids who...</p>
      <ul>
        <li><svg width="11" height="11" viewBox="0 0 11 11"><circle cx="5.5" cy="5.5" r="5.5" fill="var(--teal)"/><path d="M4.3 3 6.8 5.5 4.3 8" stroke="#fff" stroke-width="1.6" fill="none"/></svg>are home sick</li>
        <li><svg width="11" height="11" viewBox="0 0 11 11"><circle cx="5.5" cy="5.5" r="5.5" fill="var(--teal)"/><path d="M4.3 3 6.8 5.5 4.3 8" stroke="#fff" stroke-width="1.6" fill="none"/></svg>unable to go to daycare or school</li>
        <li><svg width="11" height="11" viewBox="0 0 11 11"><circle cx="5.5" cy="5.5" r="5.5" fill="var(--teal)"/><path d="M4.3 3 6.8 5.5 4.3 8" stroke="#fff" stroke-width="1.6" fill="none"/></svg>when their parent cant stay home with them.</li>
      </ul>
    </div>
    <div class="blocks-art" role="img" aria-label="Illustration of colourful toy alphabet blocks"></div>
    <p class="reassure">I know how stressful it can be when a child gets sick suddenly and unexpectedly.</p>
  </div>

  <div class="title-box front-title">
    <span class="title-box__main">COZY HOUR</span>
    <span class="title-box__script">keeper</span>
  </div>

  <p class="front-callout">I can help you<br>at last minute!</p>

  <div class="contact-box contact-box--front">
    <div class="contact-box__name">Mara Lindqvist</div>
    <div class="contact-box__phone">
      <svg width="20" height="20" viewBox="0 0 20 20" aria-hidden="true"><circle cx="10" cy="10" r="8.8" fill="none" stroke="#fff" stroke-width="1.8"/><path d="M7 5.5c-.8.5-1.3 1.3-1 2.5.7 2.6 3.3 5.3 6 6 1.2.3 2-.2 2.5-1l-1.9-1.7-1.2.8c-1-.5-2.3-1.8-2.8-2.8l.8-1.2z" fill="#fff"/></svg>
      (206) 555-0142
    </div>
  </div>
</section>

<!-- Back of postcard -->
<section class="card card--back">
  <div class="back-left">
    <svg class="tiles" width="411" height="300" aria-hidden="true">
      <rect x="0" y="0" width="90" height="110" fill="var(--tile-green)"/>
      <rect x="0" y="118" width="40" height="60" fill="var(--tile-peach)"/>
      <rect x="98" y="0" width="112" height="30" fill="var(--tile-blue)"/>
      <rect x="218" y="0" width="110" height="30" fill="var(--tile-orange)"/>
      <rect x="336" y="0" width="75" height="40" fill="var(--tile-pink)"/>
      <rect x="370" y="48" width="41" height="100" fill="var(--tile-green)"/>
    </svg>
  </div>

  <div class="title-box back-title">
    <span class="title-box__main">COZY HOUR</span>
    <span class="title-box__script">keeper</span>
  </div>

  <div class="back-panel">
    <p class="back-panel__headline">I can help you at last minute!</p>
    <p class="back-panel__message">I would like to help out those parents in need, that have pressing schedules and a sick child at home that they really want to take care of, but cant due to their work pressures and priorities.</p>
    <p class="back-panel__experience">14 years of childcare experience!</p>
  </div>

  <div class="contact-box contact-box--back">
    <div class="contact-box__name">Mara Lindqvist</div>
    <div class="contact-box__phone">
      <svg width="20" height="20" viewBox="0 0 20 20" aria-hidden="true"><circle cx="10" cy="10" r="8.8" fill="none" stroke="#fff" stroke-width="1.8"/><path d="M7 5.5c-.8.5-1.3 1.3-1 2.5.7 2.6 3.3 5.3 6 6 1.2.3 2-.2 2.5-1l-1.9-1.7-1.2.8c-1-.5-2.3-1.8-2.8-2.8l.8-1.2z" fill="#fff"/></svg>
      (206) 555-0142
    </div>
  </div>

  <div class="stamp-box"></div>
  <div class="address-line" style="top:215px"></div>
  <div class="address-line" style="top:257px"></div>
  <div class="address-line" style="top:298px"></div>
  <div class="address-line" style="top:338px"></div>
</section>

</body>
</html>
```